ONE PAGE WEB DESIGN NEEDED for Finance Company

We need a web design (ONE PAGE DESIGN ONLY) for a new finance website called Corvella Lending. Corvella Lending helps customers get the right loan, whether its a home loan, investment loan, business loan etc.

You are required to come up with just the homepage design. Professionalism and quality is the key factors in the successful design.

Here are a few design questions to help you out:

-
What information should be used on the page?
Ive provided a document which outlines all the information needed to put on homepage (attached to the brief - called corvella_page_info). Also see the Must Have section below on this brief.

-
What links should appear in the navigation/footer?:
The navigation should provide links to the following pages (NOTE: services link has subcategories):
1 Homepage
2 Services
- Home loans
- Investment loans
- Refinancing loans
- Business loans
3 About Us
4 FAQ
5 Contact Us

-
What colors should be used in the design?
Our company colors - Cyan: #2EADE3, Blue: #004B70, White. Feel free to submit designs with slight variations if you feel it improves the design.

-
What should the layout of the page be?
This is up to you to come up with - we are open to different layouts for the page design (as long as they capture the information effectively and making it easy to understand).

Target Market(s)

Potential Home owners, Families and Business Owners

Industry/Entity Type

Business

Requirements
Must have
• - Must contain our logo (attached as PNG and Illustrator file)
- Winning designer must supply a Photoshop file (PSD) that will allow us.
Nice to have
• - Should include photos/images of families, professional groups, tradespeople etc (you can use stock photos from PixelVaultImages and I will purchase them once you are selected as the winning design)
- Link to a loan calculator somewhere on front page with a button 'Find out how much you could borrow' (or maybe even try adding a loan calculator to the homepage if you think this would look good)
- Page should have a main headline "Finding the right loan for you" or "Corvella Lending finds the right loan for our customers."
- Must include Accreditation logos somewhere on the homepage (will try and supply these soon)
Should not have
• - Poor quality designs will not be considered
- Do not use clipart

```html
<!DOCTYPE html>
<html lang="en">
<head>
<meta charset="utf-8">
<title>Corvella Lending</title>
<link rel="stylesheet" href="https://fonts.googleapis.com/css2?family=Roboto+Condensed:wght@400;700&family=Arimo:wght@400&display=swap">
<style>
  :root {
    --cyan: #2eade3;
    --cyan-bright: #1ba3dc;
    --blue: #004b70;
    --navy: #0d4a6e;
    --sky-mid: #5bbfea;
    --sky-deep: #1e9bd6;
    --text: #4a4a4a;
    --muted: #6b6b6b;
    --line: #d9d9d9;
    --white: #ffffff;
  }
  * { box-sizing: border-box; margin: 0; padding: 0; }
  html, body { width: 1200px; height: 1118px; overflow: hidden; background: var(--white); }
  body { position: relative; font-family: "Arimo", Arial, sans-serif; color: var(--text); }
  .abs { position: absolute; }

  .top-rule { left: 0; top: 0; width: 1200px; height: 3px; background: var(--blue); }

  /* header */
  .brand { left: 66px; top: 78px; display: flex; align-items: center; gap: 12px; }
  .brand-dot { width: 34px; height: 34px; border-radius: 50%; background: var(--cyan); }
  .brand-name { font-family: "Roboto Condensed", sans-serif; font-weight: 700; font-size: 34px; color: var(--cyan); letter-spacing: -0.5px; }

  .contact-line { left: 862px; top: 34px; display: flex; align-items: center; gap: 8px;
    font-family: "Roboto Condensed", sans-serif; color: var(--blue); }
  .contact-line .label { font-size: 22px; font-weight: 700; }
  .contact-line .number { font-size: 25px; }

  .main-nav { left: 530px; top: 107px; width: 605px; height: 56px;
    background: linear-gradient(180deg, #1d9bd6, #0a5e8c); border-radius: 14px 14px 0 0; }
  .main-nav ul { list-style: none; display: flex; height: 56px; }
  .main-nav li { font-family: "Roboto Condensed", sans-serif; font-size: 17px; color: var(--white);
    display: flex; align-items: center; justify-content: center; height: 56px; border-right: 1px solid rgba(255,255,255,0.22); }
  .main-nav li:last-child { border-right: none; }

  /* hero */
  .hero { left: 0; top: 163px; width: 1200px; height: 330px;
    background: linear-gradient(180deg, var(--sky-mid) 0%, #8fd2f3 45%, var(--sky-deep) 100%); overflow: hidden; }
  .hero-headline { left: 70px; top: 85px; font-family: "Roboto Condensed", sans-serif; color: var(--navy); line-height: 46px; }
  .hero-headline span.lite { color: var(--white); }
  .hero-headline .l1 { font-size: 33px; }
  .hero-headline .l2 { font-size: 33px; padding-left: 80px; }
  .hero-headline .l3 { font-size: 30px; padding-left: 160px; }
  .hero-headline .big { font-size: 40px; }
  .hero-headline .bigger { font-size: 42px; }
  .hero-photo { left: 605px; top: 20px; width: 480px; height: 310px;
    background: linear-gradient(180deg, rgba(255,255,255,0.15), rgba(20,40,70,0.55)); border-radius: 40px 40px 0 0; }
  .slider-dots { left: 348px; top: 458px; display: flex; gap: 8px; }
  .slider-dots i { width: 15px; height: 15px; border-radius: 50%; background: var(--white); border: 3px solid #8fcbe8; }
  .slider-dots i.on { background: var(--blue); border-color: var(--white); }

  .dropdown { left: 650px; top: 163px; width: 164px; height: 130px; border: 1px solid #6bbfe6; border-top: none;
    border-radius: 0 0 14px 14px; background: rgba(170,220,245,0.9); padding-top: 12px; }
  .dropdown li { list-style: none; font-family: "Roboto Condensed", sans-serif; font-size: 15px; color: #1a1a1a;
    height: 28px; line-height: 24px; padding-left: 25px; margin: 0 6px; }
  .dropdown li.active { background: linear-gradient(180deg, var(--cyan), #0a7fb8); color: var(--white); border-radius: 12px; }

  /* services band */
  .services { left: 0; top: 493px; width: 1200px; height: 172px;
    background: linear-gradient(180deg, #e9e9e9 0%, #fafafa 40%, #ffffff 100%); border-bottom: 1px solid var(--line); }
  .svc { position: absolute; top: 0; height: 160px; }
  .svc + .svc { border-left: 1px solid var(--line); }
  .svc h3 { font-family: "Roboto Condensed", sans-serif; font-weight: 400; font-size: 19px; color: var(--blue);
    text-align: center; margin-top: 22px; height: 36px; }
  .svc hr { border: none; height: 2px; margin: 0 20px 16px; background: linear-gradient(90deg, transparent, #cfcfcf, transparent); }
  .svc ul { list-style: none; }
  .svc li { font-size: 14px; color: var(--text); height: 24px; white-space: nowrap; }
  .svc li::before { content: "+"; color: var(--blue); font-weight: 700; margin-right: 14px; }
  .svc li.current { color: var(--cyan); }

  .band-shadow { left: 0; top: 666px; width: 1200px; height: 30px; background: linear-gradient(180deg, #ececec, #ffffff); }

  /* about */
  .about { left: 65px; top: 706px; width: 708px; }
  .about h2 { font-family: "Roboto Condensed", sans-serif; font-weight: 400; font-size: 24px; color: var(--blue);
    padding-bottom: 8px; border-bottom: 1px dotted #555; margin-bottom: 18px; }
  .about p { font-size: 13.4px; line-height: 17px; color: var(--text); margin-bottom: 8px; }
  .about p.gap { margin-top: 14px; }
  .vdivider { left: 821px; top: 708px; height: 228px; border-left: 1px dotted #666; }

  .calc-card { left: 822px; top: 701px; width: 313px; height: 234px; border-radius: 0 18px 18px 0;
    box-shadow: 3px 4px 6px rgba(0,0,0,0.18); background: var(--white); }
  .calc-card h2 { position: absolute; left: 125px; top: 6px; font-family: "Roboto Condensed", sans-serif; font-weight: 400;
    font-size: 24px; color: var(--blue); }
  .calc-photo { position: absolute; left: 35px; top: 35px; width: 108px; height: 199px;
    background: linear-gradient(180deg, #c9ccd0, #9ea3a8 55%, #1d1d1d 100%); border-radius: 6px 6px 0 0; }
  .calc-copy { position: absolute; left: 140px; top: 57px; width: 160px; text-align: center;
    font-family: "Roboto Condensed", sans-serif; font-weight: 700; font-size: 18px; line-height: 24px; color: var(--blue); }
  .calc-btn { position: absolute; left: 170px; top: 173px; width: 119px; height: 38px; border-radius: 8px;
    background: linear-gradient(180deg, var(--cyan-bright), #0a78b0); color: var(--white); font-size: 15px;
    display: flex; align-items: center; justify-content: center; }

  /* footer */
  .footer-rule { left: 66px; top: 988px; width: 1070px; height: 6px;
    background: radial-gradient(ellipse at center, #cfcfcf 0%, rgba(255,255,255,0) 70%); }
  .footer-nav { left: 83px; top: 1024px; font-size: 13.4px; color: var(--muted); word-spacing: 2px; }
  .footer-nav span { margin: 0 6px; }
  .copyright { left: 83px; top: 1051px; font-size: 13.4px; color: var(--muted); }
  .social { left: 929px; top: 1028px; display: flex; gap: 12px; }
  .social i { width: 27px; height: 27px; border-radius: 50%; background: linear-gradient(180deg, #8a8a8a, #3d3d3d); }
</style>
</head>
<body>
  <div class="abs top-rule"></div>

  <div class="abs brand">
    <span class="brand-dot"></span>
    <span class="brand-name">Corvella Lending</span>
  </div>

  <div class="abs contact-line">
    <svg width="30" height="46" viewBox="0 0 30 46" aria-hidden="true">
      <path d="M9 4 C4 6 3 14 6 24 C9 34 15 41 21 41 L24 35 L18 30 L15 33 C12 30 10 24 10 18 L14 16 L13 8 Z" fill="#1a8fd0"/>
    </svg>
    <span class="label">Contact Us :</span><span class="number">1800 246 810</span>
  </div>

  <nav class="abs main-nav">
    <ul>
      <li style="width:105px">HOME</li>
      <li style="width:123px">SERVICES</li>
      <li style="width:128px">ABOUT US</li>
      <li style="width:92px">FAQ</li>
      <li style="width:157px">CONTACT US</li>
    </ul>
  </nav>

  <section class="abs hero">
    <h1 class="abs hero-headline">
      <div class="l1">Corvella Lending <span class="lite">finds</span></div>
      <div class="l2">the right <span class="lite big">loan</span></div>
      <div class="l3">for our <span class="lite bigger">customers.</span></div>
    </h1>
    <div class="abs hero-photo" role="img" aria-label="Photo of three smiling business professionals standing with arms crossed against a blue sky"></div>
  </section>

  <div class="abs slider-dots"><i class="on"></i><i></i><i></i><i></i></div>

  <ul class="abs dropdown">
    <li class="active">Home loans</li>
    <li>Investment loans</li>
    <li>Refinancing loans</li>
    <li>Business loans</li>
  </ul>

  <section class="abs services">
    <div class="svc" style="left:70px;width:228px">
      <h3>Home Loan</h3><hr>
      <ul style="padding-left:27px">
        <li class="current">Home buyers</li>
        <li>First home buyers</li>
        <li>Over 20 lenders</li>
      </ul>
    </div>
    <div class="svc" style="left:298px;width:257px">
      <h3>Investment Loan</h3><hr>
      <ul style="padding-left:28px">
        <li>Property investment loans</li>
        <li>Interest only loans</li>
        <li>Lorem Ipsum sit amet</li>
      </ul>
    </div>
    <div class="svc" style="left:555px;width:315px">
      <h3>Refinancing</h3><hr>
      <ul style="padding-left:34px">
        <li>Refinancing for the best rate</li>
        <li>Upsizing or downsizing</li>
        <li>Change from a variable to a fixed rate</li>
      </ul>
    </div>
    <div class="svc" style="left:870px;width:265px">
      <h3>Business Loan/Finance</h3><hr>
      <ul style="padding-left:34px">
        <li>Long term</li>
        <li>Short term</li>
        <li>Equipment and Leasing</li>
      </ul>
    </div>
  </section>
  <div class="abs band-shadow"></div>

  <section class="abs about">
    <h2>About Us</h2>
    <p>At Corvella Lending we work hard to find the right loan for our customers. We do that because we are backed by sound industry knowledge, professional experience and a great customer service approach.</p>
    <p>Corvella Lending guarantees that we will always tailor the best solution for your individual lending needs.</p>
    <p>We can do that because we have access to a wide variety of lending options from major banks to non-bank lenders and we are committed to finding the right lending product for you.</p>
    <p class="gap">There are many different loan products in the marketplace. Corvella Lending has access to a wide panel of lenders which means we can access bank and non-bank lenders that meet the individual needs of our customers.</p>
    <p>Contact Corvella Lending today on: 1800 246 810 to find out more.</p>
  </section>

  <div class="abs vdivider"></div>

  <aside class="abs calc-card">
    <h2>Loan Calculator</h2>
    <div class="calc-photo" role="img" aria-label="Photo of a hand in a business suit holding up a calculator"></div>
    <div class="calc-copy">Find out<br>how much<br>you could borrow</div>
    <div class="calc-btn">Calculator</div>
  </aside>

  <div class="abs footer-rule"></div>
  <div class="abs footer-nav">Home <span>|</span>Services<span>|</span>About US <span>|</span>FAQ <span>|</span>Contact Us</div>
  <div class="abs copyright">Copyright 2012 CorvellaLending. All Rights Reserved</div>
  <div class="abs social"><i></i><i></i><i></i><i></i><i></i></div>
</body>
</html>
```